Networking card

I just need a simple design with the following information:
Ravin Doshu
318.647.2094
rdoshu583016@mailvanta.com

I would like to have a white background with blue text like in this sample: https://cardmintly.com/business-card-207346/

```html
<!DOCTYPE html>
<html lang="en">
<head>
<meta charset="utf-8">
<title>Networking Card – Ravin Doshu</title>
<link rel="stylesheet" href="https://fonts.googleapis.com/css2?family=Montserrat:wght@300;400;600;800&display=swap">
<style>
  :root {
    --bg: #2a2a2a;
    --card: #ffffff;
    --ink: #1f1f1f;
    --accent: #e8505b;
    --muted: #3a3a3a;
  }
  * { box-sizing: border-box; margin: 0; padding: 0; }
  html, body {
    width: 1200px;
    height: 875px;
    overflow: hidden;
    background: var(--bg);
    font-family: "Montserrat", sans-serif;
  }
  .stage {
    width: 1200px;
    height: 875px;
    display: flex;
    flex-direction: column;
    align-items: center;
    justify-content: center;
    gap: 48px;
  }
  .card {
    width: 640px;
    height: 366px;
    background: var(--card);
    border-radius: 22px;
    position: relative;
    overflow: hidden;
  }
  .brand {
    display: flex;
    align-items: center;
    gap: 12px;
    color: var(--ink);
    font-weight: 800;
    letter-spacing: 0.5px;
  }
  .brand-mark {
    width: 20px;
    height: 20px;
    background: var(--accent);
    border-radius: 3px;
  }
  .card-front .brand {
    position: absolute;
    left: 50%;
    top: 50%;
    transform: translate(-50%, -50%);
    font-size: 46px;
  }
  .card-front .brand-mark { width: 30px; height: 30px; }
  .card-back .brand {
    position: absolute;
    left: 52px;
    top: 62px;
    font-size: 36px;
  }
  .card-back .brand-mark { width: 24px; height: 24px; }
  .holder {
    position: absolute;
    left: 52px;
    top: 188px;
  }
  .holder-name {
    font-size: 28px;
    color: var(--ink);
    font-weight: 800;
    line-height: 1;
  }
  .holder-name .surname {
    color: var(--accent);
    font-weight: 300;
  }
  .holder-role {
    font-size: 13px;
    color: var(--muted);
    margin-top: 4px;
  }
  .contacts {
    position: absolute;
    left: 52px;
    top: 262px;
    list-style: none;
    display: flex;
    flex-direction: column;
    gap: 8px;
  }
  .contact {
    display: flex;
    align-items: center;
    gap: 12px;
    font-size: 14px;
    color: var(--ink);
  }
  .contact svg { width: 14px; height: 14px; flex: none; }
</style>
</head>
<body>
<main class="stage">
  <section class="card card-front" aria-label="Card front">
    <div class="brand"><span class="brand-mark"></span>cardmintly</div>
  </section>

  <section class="card card-back" aria-label="Card back">
    <div class="brand"><span class="brand-mark"></span>cardmintly</div>

    <div class="holder">
      <p class="holder-name">Ravin <span class="surname">Doshu</span></p>
      <p class="holder-role">Owner</p>
    </div>

    <ul class="contacts">
      <li class="contact">
        <svg viewBox="0 0 14 14" aria-hidden="true"><rect x="3" y="0.5" width="8" height="13" rx="1.5" fill="none" stroke="#e8505b" stroke-width="1.6"/><circle cx="7" cy="11" r="0.9" fill="#e8505b"/></svg>
        318.647.2094
      </li>
      <li class="contact">
        <svg viewBox="0 0 14 14" aria-hidden="true"><rect x="0.5" y="2.5" width="13" height="9" rx="1" fill="#e8505b"/><path d="M1 3.2 L7 8 L13 3.2" fill="none" stroke="#ffffff" stroke-width="1.2"/></svg>
        rdoshu583016@mailvanta.com
      </li>
      <li class="contact">
        <svg viewBox="0 0 14 14" aria-hidden="true"><circle cx="7" cy="7" r="6.2" fill="#e8505b"/><path d="M0.8 7 H13.2 M7 0.8 C4 4 4 10 7 13.2 M7 0.8 C10 4 10 10 7 13.2" fill="none" stroke="#ffffff" stroke-width="0.9"/></svg>
        cardmintly.com
      </li>
    </ul>
  </section>
</main>
</body>
</html>
```